Women's Jewellery startup needs a captivating, beautifully designed and intuitive online store

[12/24 update]

Added 2 additional documents:

Feedback on designs received so far: designer feedback.docx
Product images from catalogue: products images.docx

Please read the feedback provided on designs provided so far to guide you further on your submission. The product images can be used to create promotional banners for the site.

@@@Added a document (VELISSE JEWELLERY_checklist.docx) which can be used by designers as a checklist when submitting their designs to ensure all aspects of the requirements have been covered @@@

+++IMPORTANT BUT NOT SPECIFIED IN THE REQUIREMENTS DOCUMENT - DESIGN SHOULD INCLUDE SUPPORT FOR MOBILE FRIENDLY SITE TOO+++

***Previous experience designing Jewellery online stores preferred (not essential)***

The name of the online Jewellery store is "Velisse Jewellery" and the business is based in Hong Kong. It will be run by 2 stay at home mothers. We need a Shopify themed store designed that will achieve the following objectives in order of priority:

• Conversion: The primary objective of the design/content is to prompt the customer to make a purchase. While this may sound obvious, it is mentioned so as not to distract the design process by focusing on other objectives (which are also important). The site also needs to be optimized so as to rank high in search engine searches for relevant keywords (SEO)
• Navigation: An intuitive interface which takes away a lot of the thinking from the customer by making it obvious what they need to do when they visit the store
• Engagement: Encourages the customer to spend time on the website and share content with their social network

Where applicable, the design of the store should reflect as closely as possible the mission statements and words outlined below:

• Jewellery you’ll fall in love with
• We want every client to leave the store with a smile
• We want to be able to provide the best service we can in every situation no matter what
• We aim to increase our business by word of mouth; therefore we tell people things about our store that makes it interesting for them to share
• We love every customer, no matter how difficult things get
• We, as a team, are so well informed about our products and brands that we always have the best information for our customers
• We celebrate women here!
• We celebrate life in here!
• We celebrate beauty here!
• We celebrate families here, as jewellery often stays within families.
• We will always try to make an extra step
• We will always try to exceed the expectation of our customers
• We will go as far as we possibly can to attract a customer back to our store and connect with us
• Every client that leaves our store knows more about jewellery because we passionately told him about it
• Romantic, classic, love, warm, cool, stylish

A draft functional specification is attached with this brief. We would like the design to reflect as closely as possible the functional requirements outlined in the document. Open to suggestions to improve upon the functional requirements.

Target Market(s)

Women aged 18-55

Industry/Entity Type

Jewelry Store

Coding

Coded - Design and coding required

Number of Pages Required

5+ page

Font styles to use
Other font styles liked:
• Myriad Pro as per Logo but open to any font that complements this one

Requirements
Must have
• 1. A look that encourages the user to make a purchase
• 2. An intuitive, easy to navigate and engaging interface
• 3. Primary colour scheme as defined in the functional specification attached
• 4. Simplistic look, not too cluttered
Nice to have
• 1. Closely matching the functional requirements of the site as outlined in the requirements specification but open to any better ideas

```html
<!DOCTYPE html>
<html lang="en">
<head>
<meta charset="utf-8">
<title>Velisse Jewellery</title>
<link href="https://fonts.googleapis.com/css2?family=Lato:ital,wght@0,400;0,700;0,900;1,400;1,700&display=swap" rel="stylesheet">
<style>
:root{
  --gold:#c18a26;
  --ink:#222;
  --bar:#e9e9e9;
  --nav-dark:#3a3a3a;
  --footer:#2d2d2d;
  --footer-base:#222;
  --card:#f2f2f2;
  --btn-grey:#666;
  --line:#d6d6d6;
  --footer-text:#b5b5b5;
}
*{box-sizing:border-box;margin:0;padding:0}
html,body{width:1200px;height:2381px;overflow:hidden}
body{font-family:"Lato",Arial,sans-serif;color:var(--ink);background:#fff;position:relative}
.abs{position:absolute}

.promo-bar{top:0;left:0;width:1200px;height:51px;background:var(--bar);display:flex;align-items:center;justify-content:center;color:var(--gold);font-weight:700;font-size:16px}
.promo-bar b{color:var(--ink);margin-left:5px}
.account-bar{top:51px;left:0;width:1200px;height:47px;background:var(--nav-dark);display:flex;align-items:center;justify-content:flex-end;padding-right:74px;color:#fff;font-size:14px;gap:10px}
.account-bar .sep{color:#aaa}
.account-bar .item{display:flex;align-items:center;gap:6px}
.account-bar .currency{margin-left:34px;margin-right:30px}
.account-bar svg{fill:#fff}

.brand{top:112px;left:75px;width:240px}
.brand .mark{display:flex;flex-direction:column;align-items:center;width:150px;gap:4px}
.brand .mark .dot{width:34px;height:34px;border-radius:50%;background:var(--gold)}
.brand .name{color:var(--gold);font-size:15px;letter-spacing:4px;font-weight:400;line-height:1}
.brand .tagline{font-style:italic;font-size:16px;margin-top:12px;white-space:nowrap}
.main-nav{top:153px;right:74px;display:flex;gap:44px;font-size:15px;font-weight:700;letter-spacing:.3px}

.hero{top:224px;left:75px;width:1051px;height:474px;overflow:hidden;
  background:
    radial-gradient(ellipse 300px 260px at 62% 42%,rgba(214,160,132,.55),rgba(214,160,132,0) 70%),
    radial-gradient(ellipse 420px 420px at 72% 55%,#6b3a26 0%,#3e2218 45%,rgba(20,16,15,0) 80%),
    linear-gradient(90deg,#111 0%,#151212 40%,#2a1a15 70%,#1c1412 100%)}
.hero h1{position:absolute;left:101px;top:174px;font-size:58px;font-weight:900;line-height:1;color:#fff}
.hero h1 span{display:block;color:var(--gold);margin-top:2px}
.hero .arrow{position:absolute;top:222px;width:34px;height:34px;border-radius:50%;background:#444;display:flex;align-items:center;justify-content:center}
.hero .arrow.prev{left:17px}.hero .arrow.next{right:17px}

.offer{top:729px;width:330px;height:236px;color:#fff;padding:0 18px 18px 16px;display:flex;flex-direction:column;justify-content:flex-end}
.offer .extra{font-weight:700;font-size:18px}
.offer .deal{color:var(--gold);font-weight:900;font-size:24px;line-height:1.18;text-transform:uppercase}
.offer .until{font-style:italic;font-weight:700;font-size:16px;margin-top:8px}
.offer.diamond{left:75px;background:radial-gradient(ellipse 140px 100px at 62% 38%,#b9d6d8,rgba(90,140,145,0) 75%),linear-gradient(150deg,#0b2224,#25555a 50%,#0a1718)}
.offer.ruby{left:434px;background:radial-gradient(ellipse 120px 100px at 52% 40%,#c21f38,#7a0d1c 55%,rgba(40,8,12,0) 90%),linear-gradient(180deg,#241014,#160608)}
.offer.gold{left:795px;background:radial-gradient(ellipse 130px 110px at 72% 42%,#d7a84b,#7d5a1f 55%,rgba(10,8,4,0) 90%),#060606}

.divider{top:1008px;left:75px;width:1051px;height:1px;background:var(--line)}
.filters{top:1044px;left:75px;width:243px}
.filter-head{display:flex;align-items:center;justify-content:space-between;height:30px;border-bottom:1px solid #bbb;color:var(--gold);font-weight:700;font-size:16px}
.filter-head .label{display:flex;align-items:center;gap:22px;padding-left:2px}
.filter-group{margin-bottom:20px}
.filter-list{list-style:none;padding-top:14px}
.filter-list li{display:flex;align-items:center;gap:22px;height:28.6px;font-size:14px}
.filter-list .box{width:11px;height:11px;border:1px solid #444;border-radius:2px}
.sidebar-rule{top:1040px;left:330px;width:1px;height:826px;background:var(--line)}

.products-title{top:1041px;left:362px;font-size:24px;font-weight:700}
.sort{top:1042px;right:74px;display:flex;align-items:center;gap:16px}
.sort .fav{color:var(--gold);font-weight:700;font-size:15px}
.sort .select{width:126px;height:32px;border:1px solid #ccc;font-size:13px;display:flex;align-items:center;justify-content:space-between;padding:0 12px}

.card{width:243px;height:344px;background:var(--card);display:flex;flex-direction:column;align-items:center;padding-top:16px}
.card .heart{position:absolute;top:16px;right:16px}
.card .photo{width:170px;height:160px;border-radius:4px}
.card .desc{margin-top:24px;font-size:14px;text-align:center;line-height:1.45;width:196px}
.card .price{color:var(--gold);font-weight:900;font-size:18px;margin-top:6px}
.card .actions{display:flex;gap:2px;margin-top:12px}
.card .btn{height:38px;width:100px;color:#fff;font-weight:700;font-size:14px;display:flex;align-items:center;justify-content:center}
.card .btn.cart{background:var(--gold)}
.card .btn.view{background:var(--btn-grey)}
.photo.emerald-ring{background:linear-gradient(135deg,#e8e4e0,#d4a58e 35%,#3f9a6c 50%,#c48d76 65%,#ece8e4)}
.photo.bracelet{background:linear-gradient(180deg,#ece9e2,#cfc6ad 35%,#f4f1e8 50%,#c4b78e 65%,#ecebe6)}
.photo.ruby-necklace{background:linear-gradient(180deg,#efe9de,#d8b777 30%,#b33444 60%,#8e1f2c 72%,#efeceb)}
.photo.earrings{background:linear-gradient(90deg,#f1ece0,#dcb24a 25%,#f0e3b0 50%,#dcb24a 75%,#f1ece0)}
.photo.sapphire-ring{background:linear-gradient(150deg,#ece6e2,#c59482 30%,#1d2b6e 50%,#101a4a 62%,#c59482 80%,#ede8e6)}
.photo.emerald-stone{background:linear-gradient(135deg,#e9f2ec,#36c066 25%,#188a3e 55%,#0f6b2e 75%,#e6efe9)}

.pager{top:1828px;left:631px;display:flex;gap:10px}
.pager span{width:32px;height:32px;border:1px solid #555;display:flex;align-items:center;justify-content:center;font-size:15px}
.pager .on{background:var(--gold);border-color:var(--gold);color:#fff;font-weight:700}

.footer{top:1898px;left:0;width:1200px;height:268px;background:var(--footer)}
.footer-col{position:absolute;top:52px}
.footer-col h3{color:var(--gold);font-size:18px;font-weight:700;margin-bottom:12px}
.footer-col a{display:block;color:var(--footer-text);font-size:14px;line-height:27px;text-decoration:none}
.newsletter{display:flex;width:269px;height:46px}
.newsletter .field{flex:1;background:#fff;font-size:13px;font-weight:700;display:flex;align-items:center;padding-left:12px}
.newsletter .go{width:47px;background:var(--gold);display:flex;align-items:center;justify-content:center}
.social{display:flex;gap:16px;margin-top:4px}
.social span{width:20px;height:20px;border-radius:50%;background:#fff}
.base{top:2166px;left:0;width:1200px;height:215px;background:var(--footer-base)}
.payments{position:absolute;top:78px;left:468px;display:flex;gap:8px}
.payments span{width:38px;height:22px;background:#e8e8e8;border-radius:2px}
.copyright{position:absolute;top:126px;width:1200px;text-align:center;color:#999;font-size:13px}
</style>
</head>
<body>
<div class="abs promo-bar">Free shipping on all orders over<b>$50</b></div>
<div class="abs account-bar">
  <span class="item"><svg width="13" height="13" viewBox="0 0 16 16"><path d="M2 12l1-4 7-7 3 3-7 7zM2 14h12v1H2z"/></svg>Sign In</span><span class="sep">/</span>
  <span class="item"><svg width="12" height="13" viewBox="0 0 16 16"><circle cx="8" cy="4.5" r="3.5"/><path d="M1 16c0-5 3-7 7-7s7 2 7 7z"/></svg>My Account</span><span class="sep">/</span>
  <span class="item"><svg width="14" height="13" viewBox="0 0 16 14"><path d="M8 14L1.5 7.5A4 4 0 018 2.5a4 4 0 016.5 5z"/></svg>Wishlist</span><span class="sep">/</span>
  <span class="item"><svg width="14" height="13" viewBox="0 0 16 14"><path d="M0 0h3l1 2h12l-2 7H5zM5 11a1.5 1.5 0 110 3 1.5 1.5 0 010-3zM13 11a1.5 1.5 0 110 3 1.5 1.5 0 010-3z"/></svg>Shopping Cart</span>
  <span class="currency">Currency: <b>HKD</b> &#8964;</span>
  <svg width="14" height="14" viewBox="0 0 16 16"><circle cx="6.5" cy="6.5" r="5" fill="none" stroke="#fff" stroke-width="2"/><path d="M10 10l5 5" stroke="#fff" stroke-width="2.4"/></svg>
</div>

<div class="abs brand">
  <div class="mark"><span class="dot"></span><span class="name">VELISSE</span></div>
  <p class="tagline">Jewellery you'll fall in love with</p>
</div>
<nav class="abs main-nav"><span>ABOUT US</span><span>SHOPPING</span><span>CUSTOMER CARE</span></nav>

<section class="abs hero" role="img" aria-label="Woman with long brown hair wearing statement earrings and a jewelled necklace against a dark background">
  <h1>We Celebrate<span>Beauty Here!</span></h1>
  <span class="arrow prev"><svg width="12" height="14" viewBox="0 0 12 14"><path d="M9 1L3 7l6 6" fill="none" stroke="#fff" stroke-width="3"/></svg></span>
  <span class="arrow next"><svg width="12" height="14" viewBox="0 0 12 14"><path d="M3 1l6 6-6 6" fill="none" stroke="#fff" stroke-width="3"/></svg></span>
</section>

<div class="abs offer diamond" role="img" aria-label="Two cut diamonds on a teal background"><span class="extra">Extra</span><span class="deal">10% OFF<br>Diamond Rings</span><span class="until">Till March 31st, 2018</span></div>
<div class="abs offer ruby" role="img" aria-label="Ruby heart pendant on a dark red background"><span class="extra">Extra</span><span class="deal">10% OFF<br>Ruby Pendant</span><span class="until">Till March 31st, 2018</span></div>
<div class="abs offer gold" role="img" aria-label="Gold signet ring on a black background"><span class="extra">Extra</span><span class="deal">10% OFF<br>Gold Rings</span><span class="until">Till March 31st, 2018</span></div>

<div class="abs divider"></div>

<aside class="abs filters">
  <div class="filter-group">
    <div class="filter-head"><span class="label"><svg width="9" height="13" viewBox="0 0 9 13"><path d="M2 1l5 5.5L2 12" fill="none" stroke="#c18a26" stroke-width="2.5"/></svg>Type</span><svg width="13" height="13" viewBox="0 0 13 13"><rect x=".5" y=".5" width="12" height="12" rx="2" fill="none" stroke="#444"/><path d="M3 6.5h7" stroke="#444"/></svg></div>
    <ul class="filter-list"><li><span class="box"></span>Rings</li><li><span class="box"></span>Necklaces</li><li><span class="box"></span>Bracelets</li><li><span class="box"></span>Earring</li><li><span class="box"></span>Charms</li></ul>
  </div>
  <div class="filter-group">
    <div class="filter-head"><span class="label"><svg width="9" height="13" viewBox="0 0 9 13"><path d="M2 1l5 5.5L2 12" fill="none" stroke="#c18a26" stroke-width="2.5"/></svg>Collection</span><svg width="13" height="13" viewBox="0 0 13 13"><rect x=".5" y=".5" width="12" height="12" rx="2" fill="none" stroke="#444"/><path d="M3 6.5h7M6.5 3v7" stroke="#444"/></svg></div>
    <ul class="filter-list"><li><span class="box"></span>Gold</li><li><span class="box"></span>Silver</li><li><span class="box"></span>Diamond</li><li><span class="box"></span>Ruby</li><li><span class="box"></span>Sapphire</li><li><span class="box"></span>Emerald</li><li><span class="box"></span>Moissanite</li></ul>
  </div>
  <div class="filter-group"><div class="filter-head"><span class="label"><svg width="9" height="13" viewBox="0 0 9 13"><path d="M2 1l5 5.5L2 12" fill="none" stroke="#c18a26" stroke-width="2.5"/></svg>Metal</span><svg width="13" height="13" viewBox="0 0 13 13"><rect x=".5" y=".5" width="12" height="12" rx="2" fill="none" stroke="#444"/><path d="M3 6.5h7M6.5 3v7" stroke="#444"/></svg></div></div>
  <div class="filter-group"><div class="filter-head"><span class="label"><svg width="9" height="13" viewBox="0 0 9 13"><path d="M2 1l5 5.5L2 12" fill="none" stroke="#c18a26" stroke-width="2.5"/></svg>Gemstone</span><svg width="13" height="13" viewBox="0 0 13 13"><rect x=".5" y=".5" width="12" height="12" rx="2" fill="none" stroke="#444"/><path d="M3 6.5h7M6.5 3v7" stroke="#444"/></svg></div></div>
  <div class="filter-group"><div class="filter-head"><span class="label"><svg width="9" height="13" viewBox="0 0 9 13"><path d="M2 1l5 5.5L2 12" fill="none" stroke="#c18a26" stroke-width="2.5"/></svg>Price Range</span><svg width="13" height="13" viewBox="0 0 13 13"><rect x=".5" y=".5" width="12" height="12" rx="2" fill="none" stroke="#444"/><path d="M3 6.5h7M6.5 3v7" stroke="#444"/></svg></div></div>
</aside>
<div class="abs sidebar-rule"></div>

<h2 class="abs products-title">Featured Products</h2>
<div class="abs sort"><span class="fav">Our Favorites</span><span class="select">What's new <span>&#8597;</span></span></div>

<div class="abs card" style="top:1097px;left:363px"><svg class="heart" width="18" height="16" viewBox="0 0 16 14"><path d="M8 14L1.5 7.5A4 4 0 018 2.5a4 4 0 016.5 5z"/></svg><div class="photo emerald-ring" role="img" aria-label="Rose gold ring set with emeralds"></div><p class="desc">Vestibulum ante ipsum primis in faucibus orci..</p><p class="price">$12.00</p><div class="actions"><span class="btn cart">Add to Cart</span><span class="btn view">Quick View</span></div></div>
<div class="abs card" style="top:1097px;left:624px"><svg class="heart" width="18" height="16" viewBox="0 0 16 14"><path d="M8 14L1.5 7.5A4 4 0 018 2.5a4 4 0 016.5 5z"/></svg><div class="photo bracelet" role="img" aria-label="Gold and crystal tennis bracelet"></div><p class="desc">Vestibulum ante ipsum primis in faucibus orci..</p><p class="price">$12.00</p><div class="actions"><span class="btn cart">Add to Cart</span><span class="btn view">Quick View</span></div></div>
<div class="abs card" style="top:1097px;left:883px"><svg class="heart" width="18" height="16" viewBox="0 0 16 14"><path d="M8 14L1.5 7.5A4 4 0 018 2.5a4 4 0 016.5 5z"/></svg><div class="photo ruby-necklace" role="img" aria-label="Gold necklace with ruby drops"></div><p class="desc">Vestibulum ante ipsum primis in faucibus orci..</p><p class="price">$12.00</p><div class="actions"><span class="btn cart">Add to Cart</span><span class="btn view">Quick View</span></div></div>
<div class="abs card" style="top:1457px;left:363px"><svg class="heart" width="18" height="16" viewBox="0 0 16 14"><path d="M8 14L1.5 7.5A4 4 0 018 2.5a4 4 0 016.5 5z"/></svg><div class="photo earrings" role="img" aria-label="Pair of gold filigree drop earrings"></div><p class="desc">Vestibulum ante ipsum primis in faucibus orci..</p><p class="price">$12.00</p><div class="actions"><span class="btn cart">Add to Cart</span><span class="btn view">Quick View</span></div></div>
<div class="abs card" style="top:1457px;left:624px"><svg class="heart" width="18" height="16" viewBox="0 0 16 14"><path d="M8 14L1.5 7.5A4 4 0 018 2.5a4 4 0 016.5 5z"/></svg><div class="photo sapphire-ring" role="img" aria-label="Rose gold ring with a large sapphire"></div><p class="desc">Vestibulum ante ipsum primis in faucibus orci..</p><p class="price">$12.00</p><div class="actions"><span class="btn cart">Add to Cart</span><span class="btn view">Quick View</span></div></div>
<div class="abs card" style="top:1457px;left:883px"><svg class="heart" width="18" height="16" viewBox="0 0 16 14"><path d="M8 14L1.5 7.5A4 4 0 018 2.5a4 4 0 016.5 5z"/></svg><div class="photo emerald-stone" role="img" aria-label="Loose emerald-cut green gemstone"></div><p class="desc">Vestibulum ante ipsum primis in faucibus orci..</p><p class="price">$12.00</p><div class="actions"><span class="btn cart">Add to Cart</span><span class="btn view">Quick View</span></div></div>

<nav class="abs pager"><span class="on">1</span><span>2</span><span>3</span><span>&middot;&middot;&middot;</span><span>&gt;&gt;</span></nav>

<footer class="abs footer">
  <div class="footer-col" style="left:75px"><h3>About Us</h3><a>Our Story</a><a>Wholesale inquiries</a></div>
  <div class="footer-col" style="left:345px"><h3>Shopping</h3><a>Orders</a><a>Wishlist</a><a>Size Guide</a></div>
  <div class="footer-col" style="left:583px"><h3>Customer Care</h3><a>Returns</a><a>FAQs</a><a>Care &amp; Warranty</a><a>Contact Us</a></div>
  <div class="footer-col" style="left:856px"><h3>Sign Up Newsletter</h3>
    <div class="newsletter"><span class="field">Email Address</span><span class="go"><svg width="18" height="10" viewBox="0 0 18 10"><path d="M0 5h15M11 1l5 4-5 4" fill="none" stroke="#fff" stroke-width="2"/></svg></span></div>
    <h3 style="margin-top:18px">Social Links</h3>
    <div class="social"><span aria-label="Social profile"></span><span aria-label="Social profile"></span><span aria-label="Social profile"></span></div>
  </div>
</footer>
<div class="abs base">
  <div class="payments" aria-label="Accepted payment methods"><span></span><span></span><span></span><span></span><span></span><span></span></div>
  <p class="copyright">Copyright &copy; 2017. Company Name. All Right Reserved</p>
</div>
</body>
</html>
```